Redo a PPT pres. - Real Estate in Brazil - Socially equitable investments in Social Housing

We need to redo the presentation attached. It is an institutional presentation to attract local and foreign investors to invest in Brazilian Social Housing Projects structured by our company "RTV".
A middle class of 100 million, a housing deficit of 9M, a strong political will & positive income generation trends constitute grounds for a significant demand in social housing.
This make a perfect scheme for investors to invest in Brazilian Social Housing.
"RTV", is a consulting "boutique" focused in Brazilian real estate, specialized in structuring, analyzing and originating Brazilian social housing projects.
RTV is part of the group RTK. RTK is structured to create value through each step of the residential real estate business - structuring, financing, sales, marketing and technology.
We would like to see designs that use mainly the color blue. The final design should communicate financial safety and professionalism. In order to reach our needs, the designer will need to have basic understanding of finance and investment in order to highlight the most important information.
The idea is to receive back the PPT with each page redesigned and an homogeneous identity.
To all designers,
Target Market(s)
Institutional Investors and wealthy individuals
Industry/Entity Type
Residential
Look and feel
Each slider illustrates characteristics of the customer's brand and the style your logo design should communicate.

```html
<!DOCTYPE html>
<html lang="en">
<head>
<meta charset="utf-8">
<title>RTV – Social Housing in Brazil</title>
<link href="https://fonts.googleapis.com/css2?family=Montserrat:wght@400;600;700;800&display=swap" rel="stylesheet">
<style>
:root{
  --stage:#000;
  --navy:#1b2a4d;
  --navy-deep:#121d38;
  --sky-top:#3d5c8c;
  --sky-mid:#6f8fb8;
  --city:#2a3f66;
  --green:#8cc63f;
  --ink:#2b3245;
  --muted:#8a93a6;
  --bar-b:#9fb3cf;
  --white:#fff;
}
*{box-sizing:border-box;margin:0;padding:0}
html,body{width:759px;height:1200px;overflow:hidden;background:var(--stage)}
body{position:relative;font-family:"Montserrat",Arial,sans-serif;color:var(--ink)}
.slide{position:absolute;width:250px;height:185px;background:var(--white);overflow:hidden}
.col-l{left:42px}.col-r{left:306px}
.row-1{top:35px}.row-2{top:228px}.row-3{top:421px}.row-4{top:614px}.row-5{top:807px}

.photo{position:absolute;top:0;left:0;bottom:0;width:118px;
  background:linear-gradient(180deg,var(--sky-top) 0%,var(--sky-mid) 38%,var(--city) 70%,var(--navy-deep) 100%)}
.photo.full{width:250px}
.tab{position:absolute;top:0;left:30px;width:58px;height:42px;background:var(--navy);
  clip-path:polygon(0 0,100% 0,100% 78%,50% 100%,0 78%)}
.brand{position:absolute;left:0;right:0;top:10px;text-align:center;color:var(--white);font:700 8px "Montserrat",sans-serif;letter-spacing:1px}
.brand::before{content:"";display:block;width:6px;height:6px;border:1px solid var(--white);border-radius:50%;margin:0 auto 3px}
.side-title{position:absolute;left:8px;width:104px;bottom:36px;color:var(--white);font:800 8px/1.2 "Montserrat",sans-serif;text-transform:uppercase}
.foot{position:absolute;left:0;bottom:0;width:118px;height:22px;background:var(--navy);padding:4px 8px;color:var(--green);font:600 3.6px/1.4 "Montserrat",sans-serif}
.badge{position:absolute;left:36px;top:54px;width:46px;height:46px;border-radius:50%;background:var(--white);
  border:2px solid rgba(255,255,255,.55);box-shadow:0 0 0 3px rgba(255,255,255,.25);
  display:flex;align-items:center;justify-content:center;text-align:center;color:var(--navy);font:600 4.2px/1.3 "Montserrat",sans-serif;padding:4px}
.pager{position:absolute;right:8px;bottom:6px;font:600 4px "Montserrat",sans-serif;color:var(--muted)}
.pager b{color:var(--navy)}

.content{position:absolute;left:126px;top:12px;width:116px}
.bar-head{background:var(--navy);color:var(--white);font:700 4.2px "Montserrat",sans-serif;padding:2.5px 4px;margin:6px 0 3px;text-transform:uppercase}
.bar-head:first-child{margin-top:0}
.txt{font:400 3.2px/1.45 "Montserrat",sans-serif;color:var(--ink)}
.txt b{font-weight:700}
ul.txt{list-style:none}
ul.txt li{padding-left:4px;position:relative;margin-bottom:1.2px}
ul.txt li::before{content:"";position:absolute;left:0;top:1.4px;width:1.6px;height:1.6px;background:var(--navy)}

/* cover */
.cover-banner{position:absolute;left:62px;top:0;width:126px;height:148px;background:var(--navy);
  clip-path:polygon(0 0,100% 0,100% 80%,50% 100%,0 80%);text-align:center;padding-top:12px}
.cover-banner .brand{position:static;margin-bottom:28px}
.cover-title{color:var(--white);font:800 9px/1.2 "Montserrat",sans-serif;margin-bottom:8px}
.cover-sub{color:var(--green);font:600 5.4px/1.3 "Montserrat",sans-serif;padding:0 14px}

/* agenda */
.agenda{position:absolute;left:140px;top:16px;width:102px;list-style:none}
.agenda li{display:flex;align-items:center;margin-bottom:5.4px}
.num{flex:none;width:13px;height:13px;border-radius:50%;background:var(--green);color:var(--white);font:700 5px "Montserrat",sans-serif;display:flex;align-items:center;justify-content:center;margin-right:6px}
.agenda strong{display:block;font:700 4px/1.2 "Montserrat",sans-serif;color:var(--ink)}
.agenda span{display:block;font:400 3px "Montserrat",sans-serif;color:var(--muted)}

/* full-photo section slides */
.section-badge{left:20px;top:66px}
.section-title{position:absolute;left:130px;top:112px;width:112px;color:var(--green);font:800 9px/1.15 "Montserrat",sans-serif;text-transform:uppercase}
.section-title.white{color:var(--white)}
</style>
</head>
<body>

<!-- Cover -->
<section class="slide col-l row-1">
  <div class="photo full" role="img" aria-label="City skyline of high-rise towers under a blue sky"></div>
  <div class="cover-banner">
    <div class="brand">RTV</div>
    <div class="cover-title">SOCIAL HOUSING<br>IN BRAZIL</div>
    <div class="cover-sub">HIGH YIELD RETURN FOR A QUASI SOVEREIGN RISK</div>
  </div>
</section>

<!-- How to invest -->
<section class="slide col-r row-1">
  <div class="photo" role="img" aria-label="City skyline of high-rise towers"></div>
  <div class="tab"><div class="brand">RTV</div></div>
  <div class="side-title">How to invest in social housing in Brazil?</div>
  <div class="foot">A tangible investment in residential assets</div>
  <svg class="cycle" style="position:absolute;left:124px;top:8px" width="122" height="170" viewBox="0 0 122 170" font-family="Montserrat,sans-serif" font-size="3" font-weight="600" fill="#2b3245" text-anchor="middle">
    <circle cx="61" cy="80" r="44" fill="none" stroke="#8cc63f" stroke-width="1"/>
    <g stroke="#8cc63f" stroke-width="1" fill="#fff">
      <circle cx="61" cy="36" r="15"/><circle cx="92" cy="49" r="15"/><circle cx="105" cy="80" r="15"/><circle cx="92" cy="111" r="15"/>
      <circle cx="61" cy="124" r="15"/><circle cx="30" cy="111" r="15"/><circle cx="17" cy="80" r="15"/><circle cx="30" cy="49" r="15"/>
    </g>
    <text x="61" y="32">Building<tspan x="61" dy="3.6">housing units</tspan><tspan x="61" dy="3.6">for middle</tspan><tspan x="61" dy="3.6">class buyers</tspan></text>
    <text x="92" y="47">Investing in<tspan x="92" dy="3.6">individual</tspan><tspan x="92" dy="3.6">projects</tspan></text>
    <text x="105" y="78">Specialized<tspan x="105" dy="3.6">financial</tspan><tspan x="105" dy="3.6">vehicle</tspan></text>
    <text x="92" y="107">Construction<tspan x="92" dy="3.6">with local</tspan><tspan x="92" dy="3.6">partners</tspan></text>
    <text x="61" y="122">Co-financed<tspan x="61" dy="3.6">by government</tspan></text>
    <text x="30" y="107">Equity<tspan x="30" dy="3.6">participation</tspan><tspan x="30" dy="3.6">of RTV or</tspan><tspan x="30" dy="3.6">sellers</tspan></text>
    <text x="17" y="78">Pre-sales<tspan x="17" dy="3.6">before</tspan><tspan x="17" dy="3.6">delivery</tspan></text>
    <text x="30" y="47">Target IRR<tspan x="30" dy="3.6">20-30%</tspan></text>
  </svg>
  <div class="pager">‹ <b>02</b> ›</div>
</section>

<!-- Agenda -->
<section class="slide col-l row-2">
  <div class="photo" role="img" aria-label="City skyline of high-rise towers"></div>
  <div class="tab"><div class="brand">RTV</div></div>
  <div class="side-title">The time is now !</div>
  <div class="foot">The time is now to invest</div>
  <ol class="agenda">
    <li><span class="num">1</span><div><strong>Macro-environment &amp; Mortgage market</strong><span>Green light</span></div></li>
    <li><span class="num">2</span><div><strong>A sophisticated &amp; successful program</strong><span>Proven model</span></div></li>
    <li><span class="num">3</span><div><strong>Investment Structure of a typical project</strong><span>Average financial flows</span></div></li>
    <li><span class="num">4</span><div><strong>Small &amp; mid size developers</strong><span>Key partners</span></div></li>
    <li><span class="num">5</span><div><strong>RTV</strong><span>Value added &amp; risk mitigation</span></div></li>
    <li><span class="num">6</span><div><strong>RTK</strong><span>RTK, part of an integrated family of companies</span></div></li>
    <li><span class="num">7</span><div><strong>Appendix</strong><span>Summary, RTV track record</span></div></li>
  </ol>
  <div class="pager">‹ <b>03</b> ›</div>
</section>

<!-- Macro section -->
<section class="slide col-r row-2">
  <div class="photo full" role="img" aria-label="City skyline of high-rise towers under a blue sky"></div>
  <div class="tab"><div class="brand">RTV</div></div>
  <div class="badge section-badge">Green Light</div>
  <div class="section-title">Macro-environment &amp; mortage market</div>
</section>

<!-- Middle class -->
<section class="slide col-l row-3">
  <div class="photo" role="img" aria-label="City skyline of high-rise towers"></div>
  <div class="tab"><div class="brand">RTV</div></div>
  <div class="badge">Green Light</div>
  <div class="side-title">A middle class of 100 million people</div>
  <div class="foot">Strong political will &amp; positive income generation trends ground a significant demand in social housing</div>
  <div class="content">
    <div class="bar-head">Politics</div>
    <p class="txt">Brazil benefited from political stability for over 18 years with the federal government.</p>
    <p class="txt">The country aims to end its housing deficit and has launched a national housing program.</p>
    <p class="txt"><b>Growth Acceleration Program (2007-10): R$ 600B</b></p>
    <ul class="txt"><li>Public investment in infrastructure</li><li>Launch of the national housing program</li><li>Stimulating credit &amp; financing to the real estate sector</li></ul>
    <div class="bar-head">Emergence of the middle class</div>
    <ul class="txt">
      <li>Household income grew sharply, the middle class went from <b>38%</b> of population in 2003 to more than <b>50%</b> in 2011.</li>
      <li>More than <b>100 million people</b> now belong to the <b>middle class</b>. They need decent housing.</li>
      <li><b>Middle class</b> will represent <b>58%</b> of the population by 2014.</li>
      <li>Consolidation of a large middle class with appetite for premium products.</li>
      <li>Housing deficit is estimated to be around <b>9M</b>, a clear demand driver.</li>
    </ul>
  </div>
  <div class="pager">‹ <b>05</b> ›</div>
</section>

<!-- Still growing -->
<section class="slide col-r row-3">
  <div class="photo" role="img" aria-label="City skyline of high-rise towers"></div>
  <div class="tab"><div class="brand">RTV</div></div>
  <div class="badge">Green Light</div>
  <div class="side-title">And still growing.....!</div>
  <div class="foot">Positive demographics &amp; economic environment stimulate the demand</div>
  <div class="content">
    <div class="bar-head">Number of people based on ages</div>
    <svg width="116" height="58" viewBox="0 0 116 58" font-family="Montserrat,sans-serif" font-size="2.8" fill="#8a93a6">
      <line x1="22" y1="2" x2="22" y2="46" stroke="#c9cfd9" stroke-width=".4"/>
      <line x1="22" y1="46" x2="112" y2="46" stroke="#c9cfd9" stroke-width=".4"/>
      <text x="20" y="8" text-anchor="end">60-74 years</text>
      <rect x="22" y="4" width="40" height="2.6" fill="#1b2a4d"/><rect x="22" y="7" width="56" height="2.6" fill="#9fb3cf"/>
      <text x="20" y="19" text-anchor="end">45-59 years</text>
      <rect x="22" y="15" width="58" height="2.6" fill="#1b2a4d"/><rect x="22" y="18" width="70" height="2.6" fill="#9fb3cf"/>
      <text x="20" y="30" text-anchor="end">30-44 years</text>
      <rect x="22" y="26" width="72" height="2.6" fill="#1b2a4d"/><rect x="22" y="29" width="78" height="2.6" fill="#9fb3cf"/>
      <text x="20" y="41" text-anchor="end">15-29 years</text>
      <rect x="22" y="37" width="84" height="2.6" fill="#1b2a4d"/><rect x="22" y="40" width="76" height="2.6" fill="#9fb3cf"/>
      <text x="22" y="50" text-anchor="middle">0</text><text x="52" y="50" text-anchor="middle">20</text><text x="82" y="50" text-anchor="middle">40</text><text x="112" y="50" text-anchor="middle">60</text>
      <rect x="36" y="53" width="3" height="3" fill="#1b2a4d"/><text x="41" y="55.6">2000 (in M)</text>
      <rect x="70" y="53" width="3" height="3" fill="#9fb3cf"/><text x="75" y="55.6">2020 (in M)</text>
    </svg>
    <div class="bar-head">End buyers</div>
    <ul class="txt">
      <li>Aging population: average number of persons per household falls from 3.7 in 1991 to 3.1 in 2010.</li>
      <li>Population of 194 million people by 2025, fueling new household formation.</li>
      <li>Low and stable unemployment rate, 6%.</li>
      <li>Consolidation of credit: mortgage volume grew over 40% a year since 2005.</li>
    </ul>
  </div>
  <div class="pager">‹ <b>06</b> ›</div>
</section>

<!-- RTK section -->
<section class="slide col-l row-4">
  <div class="photo full" role="img" aria-label="City skyline of high-rise towers under a blue sky"></div>
  <div class="tab"><div class="brand">RTV</div></div>
  <div class="badge section-badge">RTV, Part of An Integrated Family of companies</div>
  <div class="section-title white" style="top:124px;left:24px">RTK</div>
</section>

<!-- RTK focus -->
<section class="slide col-r row-4">
  <div class="photo" role="img" aria-label="City skyline of high-rise towers"></div>
  <div class="tab"><div class="brand">RTV</div></div>
  <div class="badge">RTV, Part of An Integrated Family of companies</div>
  <div class="side-title">RTK focus</div>
  <div class="foot">A focus on social housing and brokerage supported by strong technology and an online marketing platform</div>
  <div class="content">
    <div class="bar-head">The online housing</div>
    <ul class="txt">
      <li>Concentrated in the hands of few small developers and brokers with limited reach.</li>
      <li>Small and mid-size developers lack an online presence to reach buyers.</li>
      <li>Buyers search online first but find fragmented and outdated offers.</li>
      <li>As a response, RTK offers the services of an online housing platform and consulting.</li>
    </ul>
    <div class="bar-head">The brokerage market</div>
    <ul class="txt">
      <li>Real estate brokerage in Brazil is still fragmented and informal.</li>
      <li>The residential segment is growing fast with strong local demand.</li>
      <li>Most small developers lack their own sales team and need partners.</li>
      <li><b>RTK</b> created a brokerage unit to offer developers a complete sales channel.</li>
      <li><b>RTK</b> also started working with partner brokers, allowing developers to reach buyers nationwide.</li>
    </ul>
  </div>
  <div class="pager">‹ <b>10</b> ›</div>
</section>

<!-- RTK focus continued -->
<section class="slide col-l row-5">
  <div class="photo" role="img" aria-label="City skyline of high-rise towers"></div>
  <div class="tab"><div class="brand">RTV</div></div>
  <div class="badge">RTV, Part of An Integrated Family of companies</div>
  <div class="side-title">RTK focus<br>(continue)</div>
  <div class="foot">A focus on social housing and brokerage supported by strong technology and an online marketing platform</div>
  <div class="content">
    <div class="bar-head">The technology</div>
    <ul class="txt">
      <li>Technology is <b>RTK</b> core focus: it connects the real estate market with an efficient and scalable brokerage and online housing service.</li>
      <li>Its proprietary platform brings together developers, brokers and buyers on a single system, tracking each sale from lead to contract.</li>
      <li>Developers follow their projects in real time, with full visibility on stock, prices and the status of every unit.</li>
      <li>Brokers use mobile tools to register visits and manage their clients, raising conversion and shortening sales cycles.</li>
      <li>With a single database, <b>RTK</b> measures demand by region and income band, which feeds project structuring.</li>
      <li>The platform automates documentation and mortgage approval steps, reducing cost and delays for buyers.</li>
      <li><b>RTK</b> connects all players, from the developer to the final customer, through one unique offering.</li>
    </ul>
  </div>
  <div class="pager">‹ <b>11</b> ›</div>
</section>

</body>
</html>
```